Brell Harbor Company Business Cards

Front and Back Business Card - logo and text setup - cool design. I need workable photoshop or illustrator files so I can setup each employee card with design that is created
Updates

Hi everyone, thank you for the great entries. Please no more white and blue cards - there are so many already - black and silver only now please. thanks!

Target Market(s)

Construction Industry - Facility Managers

Industry/Entity Type

Construction

Contact Information for Business Card

I really like contemporary simplistic looks - clean neat....not opposed to seeing some black backrounds

Requirements
Must have
• Logo/website address with design on front only - www.brellharbor-example.com (logo attached)
• Back:
• Name/Title/Company Address/Phone/email address
Nice to have
• Cool design
Should not have
• Nothing gimmicky like Fire or Water - since we are a Fire Protection company - it has all been done

```html
<!DOCTYPE html>
<html lang="en">
<head>
<meta charset="utf-8">
<title>Brell Harbor Company – Business Cards</title>
<link rel="stylesheet" href="https://fonts.googleapis.com/css2?family=Lato:wght@300;400;700;900&family=Oswald:wght@500&display=swap">
<style>
  :root {
    --backdrop: #161617;
    --card: #2a2a2c;
    --silver-light: #f2f2f4;
    --silver-mid: #b9b9bd;
    --silver-dark: #7d7d82;
    --accent-blue: #3b4a8c;
    --text-grey: #c9c9cc;
    --text-soft: #9a9a9e;
    --rule: #6d6d72;
  }
  * { box-sizing: border-box; margin: 0; padding: 0; }
  html, body {
    width: 1200px; height: 912px; overflow: hidden;
    background: var(--backdrop);
    font-family: "Lato", sans-serif;
  }
  .sheet {
    position: relative; width: 1200px; height: 912px;
    display: flex; flex-direction: column; align-items: center;
    justify-content: center; gap: 40px;
  }
  .card {
    position: relative; width: 700px; height: 400px;
    background: var(--card);
    overflow: hidden;
    box-shadow: 0 10px 30px rgba(0,0,0,.5);
  }
  .card-edges { position: absolute; inset: 0; width: 100%; height: 100%; }

  /* Front */
  .brand {
    position: absolute; left: 0; right: 0; top: 140px;
    display: flex; align-items: center; justify-content: center; gap: 18px;
  }
  .brand-mark { width: 34px; height: 34px; background: var(--silver-mid); }
  .brand-name {
    font-family: "Lato", sans-serif; font-weight: 900;
    font-size: 46px; letter-spacing: -0.5px; color: var(--silver-mid);
  }
  .front-web {
    position: absolute; left: 0; right: 0; top: 262px;
    text-align: center; font-size: 17px; font-weight: 400;
    color: var(--text-grey); letter-spacing: .5px;
  }

  /* Back */
  .person {
    position: absolute; right: 330px; top: 196px; text-align: right;
  }
  .person-name {
    font-family: "Oswald", sans-serif; font-weight: 500;
    font-size: 28px; color: var(--accent-blue); letter-spacing: .3px;
    text-transform: uppercase; white-space: nowrap;
  }
  .person-title {
    font-size: 19px; font-weight: 400; color: var(--text-grey); margin-top: 2px;
  }
  .divider {
    position: absolute; left: 394px; top: 148px; width: 1px; height: 150px;
    background: var(--rule);
  }
  .contact {
    position: absolute; left: 418px; top: 146px; color: var(--text-grey);
    font-size: 16px; font-weight: 400; line-height: 1.35;
  }
  .contact-address { margin-bottom: 14px; }
  .contact-list { list-style: none; }
  .contact-list li { display: flex; align-items: center; gap: 10px; }
  .contact-icon { width: 13px; height: 13px; flex: none; fill: var(--accent-blue); }
</style>
</head>
<body>
<main class="sheet">

  <section class="card card-front" aria-label="Card front">
    <svg class="card-edges" viewBox="0 0 700 400" preserveAspectRatio="none" aria-hidden="true">
      <defs>
        <linearGradient id="silverLeft" x1="0" y1="0" x2="1" y2="0">
          <stop offset="0" stop-color="var(--silver-dark)"/>
          <stop offset=".55" stop-color="var(--silver-light)"/>
          <stop offset="1" stop-color="var(--silver-mid)"/>
        </linearGradient>
        <linearGradient id="silverRight" x1="1" y1="0" x2="0" y2="0">
          <stop offset="0" stop-color="var(--silver-dark)"/>
          <stop offset=".55" stop-color="var(--silver-light)"/>
          <stop offset="1" stop-color="var(--silver-mid)"/>
        </linearGradient>
      </defs>
      <path d="M0,0 Q100,200 0,400 Z" fill="var(--accent-blue)"/>
      <path d="M0,0 Q92,200 0,400 Z" fill="url(#silverLeft)"/>
      <path d="M700,0 Q600,200 700,400 Z" fill="var(--accent-blue)"/>
      <path d="M700,0 Q608,200 700,400 Z" fill="url(#silverRight)"/>
    </svg>
    <div class="brand">
      <span class="brand-mark"></span>
      <span class="brand-name">Brell Harbor Company</span>
    </div>
    <p class="front-web">www.brellharbor-example.com</p>
  </section>

  <section class="card card-back" aria-label="Card back">
    <svg class="card-edges" viewBox="0 0 700 400" preserveAspectRatio="none" aria-hidden="true">
      <defs>
        <linearGradient id="silverBand" x1="0" y1="0" x2="1" y2="0">
          <stop offset="0" stop-color="var(--silver-dark)"/>
          <stop offset=".5" stop-color="var(--silver-light)"/>
          <stop offset="1" stop-color="var(--silver-mid)"/>
        </linearGradient>
      </defs>
      <rect x="0" y="388" width="700" height="12" fill="url(#silverBand)"/>
    </svg>

    <div class="person">
      <p class="person-name">Marla Quinn Devereaux</p>
      <p class="person-title">President</p>
    </div>

    <div class="divider"></div>

    <div class="contact">
      <p class="contact-address">48 Ridgeway Lane<br>Port Alden, NY 10990</p>
      <ul class="contact-list">
        <li>
          <svg class="contact-icon" viewBox="0 0 16 16" aria-hidden="true"><path d="M3.6 1.2l2.3 2.6-1.3 1.8c.9 2 2.4 3.5 4.4 4.5l1.8-1.3 2.6 2.3-1.2 2.1C6.9 14.8 1.2 9.1 1.3 2.4z"/></svg>
          <span>(555) 013-4470</span>
        </li>
        <li>
          <svg class="contact-icon" viewBox="0 0 16 16" aria-hidden="true"><path d="M1 3h14v10H1z M1.8 3.8L8 8.6l6.2-4.8" stroke="var(--card)" stroke-width="1"/></svg>
          <span>info@brellharbor-example.com</span>
        </li>
        <li>
          <svg class="contact-icon" viewBox="0 0 16 16" aria-hidden="true"><circle cx="8" cy="8" r="7"/><path d="M1 8h14M8 1c-3 3.5-3 10.5 0 14M8 1c3 3.5 3 10.5 0 14" stroke="var(--card)" stroke-width="1" fill="none"/></svg>
          <span>www.brellharbor-example.com</span>
        </li>
      </ul>
    </div>
  </section>

</main>
</body>
</html>
```